Vocational Mentor needs an impressive business card

1. I need a business card (or maybe three with identic look) to promote me and my three business titles/services:
- Vocational Mentor. I help people find their vocation and live happily from it. I use my 20 years of experience in business, management and psychology to help them identify the most efficient ways to make a living doing what they are passionate about.
- Business Angel. I help founders start a succesful business with minimum risks and costs. I use my 20 years of experience in sales, management and entrepreneurship to help them identify the most efficient ways, in terms of time and cost, to validate their business idea.
- Learning Designer. I design unique learning programs that produce long-term cognitive and behavioural changes to people and organisations. I use my 20 years of experience in learning, teaching and change management to create minimalist experiences and processes that allow them to change efficiently in their pursued direction.

2. I would like a two-sided business card, on the front with my name, contact details and titles, on the back the explanation of the services.
Updates

Hi all,

I updated my brief, included contacts info and give feedback on all designs I got. I am new on this platform so please tell me if you need anything else or if I don't use corectly the platform forms.

Kind regards,
Tudor

Hi all,

I shortened the services description by deleting the phrase "I call..."

Kind regards,
Tudor

Target Market(s)

Freelancers, startups, people and organization willing to invest in change through ultimate learning experiences

Industry/Entity Type

Business

Font styles to use
Serif

Requirements
Must have
• Front side: full name, titles, web site, email, phone like below:
Tudor Vasilache
Vocational Mentor, Business Angel, Learning Designer
info@tudorvasilache.example
www.tudorvasilache.example
+40-745-TUDORV
Nice to have
• Back side: the description of the services I provide as in the task description.
1/3: it would be nice if I can jam all three titles on the front side but then I need a solution to jam all three services on the back side.

```html
<!DOCTYPE html>
<html lang="en">
<head>
<meta charset="utf-8">
<title>Tudor Vasilache – Business Card</title>
<link rel="stylesheet" href="https://fonts.googleapis.com/css2?family=Source+Serif+4:opsz,wght@8..60,300;8..60,400;8..60,600&display=swap">
<style>
  :root {
    --backdrop: #d9d6d1;
    --paper: #ebe8df;
    --ink-red: #a8191b;
    --ink-light: #fbf3ea;
    --red-deep: #a3120f;
    --red-mid: #c8290f;
    --orange: #e0561b;
  }
  * { box-sizing: border-box; margin: 0; padding: 0; }
  html, body { width: 1200px; height: 900px; overflow: hidden; }
  body {
    background: var(--backdrop);
    font-family: "Source Serif 4", Georgia, serif;
    position: relative;
  }
  .card {
    position: absolute;
    top: 135px;
    width: 360px;
    height: 628px;
    background: var(--paper);
    box-shadow: 0 2px 6px rgba(0,0,0,.18);
    overflow: hidden;
  }
  .card--front { left: 213px; }
  .card--back { left: 625px; }
  .card__field { position: absolute; left: 0; top: 0; width: 360px; height: 628px; }
  .front__name {
    position: absolute; left: 36px; top: 122px;
    color: var(--ink-light);
    font-weight: 300; font-size: 44px; line-height: 46px;
    letter-spacing: -0.5px;
  }
  .front__titles {
    position: absolute; left: 37px; top: 287px;
    list-style: none;
    color: var(--ink-red);
    font-weight: 600; font-size: 14.5px; line-height: 24px;
    letter-spacing: 1.1px; text-transform: uppercase;
  }
  .front__contact {
    position: absolute; left: 37px; top: 549px;
    color: var(--ink-red);
    font-size: 20px; line-height: 25px; font-style: normal;
  }
  .services {
    position: absolute; left: 35px; top: 35px; width: 300px;
    color: var(--ink-light);
  }
  .service { margin-bottom: 15px; }
  .service__title {
    font-weight: 600; font-size: 14.5px; line-height: 18px;
    letter-spacing: 1px; text-transform: uppercase;
  }
  .service__text { font-size: 14.6px; line-height: 18px; font-weight: 400; }
  .back__web {
    position: absolute; left: 35px; top: 573px;
    color: var(--ink-red);
    font-weight: 600; font-size: 20px; letter-spacing: 0.2px;
  }
</style>
</head>
<body>
  <section class="card card--front">
    <svg class="card__field" viewBox="0 0 360 628" role="img" aria-label="Abstract red and orange geometric pattern">
      <defs>
        <linearGradient id="frontRed" x1="0" y1="0" x2="1" y2="1">
          <stop offset="0" stop-color="var(--orange)"/>
          <stop offset="0.45" stop-color="var(--red-deep)"/>
          <stop offset="1" stop-color="var(--orange)"/>
        </linearGradient>
      </defs>
      <polygon points="0,0 360,0 360,235 62,266 0,250" fill="url(#frontRed)"/>
    </svg>
    <h1 class="front__name">Tudor<br>Vasilache</h1>
    <ul class="front__titles">
      <li>Vocational Mentor</li>
      <li>Business Angel</li>
      <li>Learning Designer</li>
    </ul>
    <address class="front__contact">
      +40-745-TUDORV<br>
      info@tudorvasilache.example
    </address>
  </section>

  <section class="card card--back">
    <svg class="card__field" viewBox="0 0 360 628" role="img" aria-label="Abstract red and orange geometric pattern">
      <defs>
        <linearGradient id="backRed" x1="0" y1="0" x2="1" y2="1">
          <stop offset="0" stop-color="var(--red-mid)"/>
          <stop offset="0.5" stop-color="var(--red-deep)"/>
          <stop offset="1" stop-color="var(--orange)"/>
        </linearGradient>
      </defs>
      <polygon points="0,0 360,0 360,525 60,555 0,508" fill="url(#backRed)"/>
    </svg>
    <div class="services">
      <article class="service">
        <h2 class="service__title">Vocational Mentor</h2>
        <p class="service__text">I help people to find their vocation and live happily from it. I use my 20 years of experience in business, management and psychology to help them identify the most efficient ways to make a living doing what they are passionate about.</p>
      </article>
      <article class="service">
        <h2 class="service__title">Business Angel</h2>
        <p class="service__text">I help founders to start a successful business with minimum risks and costs. I use my 20 years of experience in sales, management and entrepreneurship to help them identify the most efficient ways, in terms of time and cost, to validate their business idea.</p>
      </article>
      <article class="service">
        <h2 class="service__title">Learning Designer</h2>
        <p class="service__text">I design unique learning programs that produce long-term cognitive and behavioural changes to people and organisations. I use my 20 years of experience in learning, teaching and change management to create minimalist experiences and processes that allows them to change efficiently in their pursued direction.</p>
      </article>
    </div>
    <p class="back__web">www.tudorvasilache.example</p>
  </section>
</body>
</html>
```